Verpackungsdesign für Räucherstäbchen
Zielgruppe
Unsere Firma Lindenkram importiert hochwertige und reine Räucherstoffe aus entfernten Ländern. Dabei steht die Nachhaltigkeit und der faire Handel im Vordergrund. Unser Fokus ist dabei der Handel mit Weihrauch, den wir aus den Ursprungsländern importieren und an Großhändler, Händler und Endkunden weiterverkaufen. Seit einigen Jahren haben wir den Wunsch echte, natürliche Räucherstäbchen auf den Markt zu bringen. Dieses Projekt wurde nun umgesetzt.
Wir suchen ein Verpackungsdesign für unsere Räucherstäbchen. Die Räucherstäbchen sind absolut naturrein (95% aller Räucherstäbchen auf dem Markt sind es nicht), ohne Chemie, ohne Parfum, ohne Synthetik. Absolut rein, hergestellt aus besten Rohstoffen, teilweise direkt aus Deutschland.
Aufgabenstellung
Da die Räucherstäbchen auch in den Handel kommen werden, ist es am Besten, dass die Verpackung eine Faltschachtel ist mit den Maßen: 6cm Breite, 22cm Länge, 1,5cm Höhe
Die Schachtel sollte sehr natürlich ausschauen und die Farben nicht zu kräftig.
Es wird ein Logo darauf geben, das ich hochladen werde.
Farben sollten natürlich sein, Elegant und natürlich. Wir wissen nicht genau, wie die Verpackung aussehen soll, doch sicher ist, dass sie nicht zu überladen sein sollte. Die Verpackung sollte schlicht, natürlich und edel sein
Wir planen über 20 Sorten: Harze, Sandelholz, Patchouli etc.
Das Design der Verpackung sollte das berücksichtigen. Ein Design, das später an die verschiedenen Sorten angepasst werden kann
Für das Beispiel-Design:
Text auf der Vorderseite:
Räucherstäbchen
Weihrauch Afrika
Made with love in Germany
Natur pur
Rückseite:
Naturreine Räucherstäbchen hergestellt mit den reinsten Rohstoffen
Ohne chemische oder synthetische Zusätze, kein Parfum, keine Abbrennhilfe
Brenndauer: ca. 45- 60min
Eine Verpackung beinhaltet 10 Räucherstäbchen.
Hergestellt von:
Made by
Lindenkram
Birkenauer Weg 14
61287 Wiesental

```html
<!DOCTYPE html>
<html lang="de">
<head>
<meta charset="utf-8">
<title>Lindenkram – Räucherstäbchen Faltschachtel</title>
<link rel="stylesheet" href="https://fonts.googleapis.com/css2?family=Oswald:wght@300;400;500&display=swap">
<style>
  :root {
    --stage: #e9e9e9;
    --paper: #efebe2;
    --green: #5e8a4b;
    --green-text: #4e7a3e;
    --green-soft: #8fae7f;
    --brown-text: #776b61;
    --layer-1: #e0d9cf;
    --layer-2: #cbc2b7;
    --layer-3: #b1a79c;
    --layer-4: #9d9288;
    --white: #ffffff;
  }
  * { margin: 0; padding: 0; box-sizing: border-box; }
  html, body { width: 1200px; height: 1200px; overflow: hidden; }
  body {
    background: var(--stage);
    font-family: "Oswald", sans-serif;
    position: relative;
  }
  .panel {
    position: absolute;
    top: 117px;
    width: 268px;
    height: 980px;
    background: var(--paper);
    overflow: hidden;
  }
  .panel--front { left: 232px; }
  .panel--back { left: 656px; }

  .brand {
    position: absolute;
    top: 96px;
    left: 0; right: 0;
    text-align: center;
  }
  .brand__mark {
    display: block;
    width: 94px; height: 94px;
    margin: 0 auto 12px;
    border: 1.5px solid var(--green-soft);
    border-radius: 50%;
  }
  .brand__name {
    font-size: 19px;
    font-weight: 500;
    color: var(--green-text);
    letter-spacing: 0.3px;
    line-height: 1;
  }

  .product-title {
    position: absolute;
    top: 330px;
    left: 0; right: 0;
    text-align: center;
    color: var(--green-text);
    font-weight: 400;
    text-transform: uppercase;
    line-height: 36px;
  }
  .product-title__type { font-size: 27px; display: block; letter-spacing: 0.3px; }
  .product-title__variety { font-size: 24px; display: block; }

  .band {
    position: absolute;
    top: 476px;
    left: 0;
    width: 268px;
    height: 140px;
  }
  .band__claim {
    position: absolute;
    top: 496px;
    left: 0; right: 0;
    text-align: center;
    color: var(--white);
    font-size: 20px;
    font-weight: 400;
    line-height: 1.2;
    text-transform: uppercase;
  }
  .script-mark {
    position: absolute;
    border-radius: 4px;
    background: var(--green-soft);
  }
  .script-mark--front { top: 612px; left: 30px; width: 210px; height: 78px; opacity: 0.45; }
  .script-mark--back { top: 500px; left: 64px; width: 140px; height: 46px; opacity: 0.55; }

  .leaf-art {
    position: absolute;
    top: 700px;
    left: 14px;
    width: 240px;
    height: 138px;
    border-radius: 6px;
    background: linear-gradient(180deg, rgba(126,160,108,0.18), rgba(126,160,108,0.32));
  }

  .base {
    position: absolute;
    left: 0; bottom: 0;
    width: 268px;
    height: 134px;
  }

  .copy {
    position: absolute;
    left: 0; right: 0;
    text-align: center;
    font-weight: 400;
  }
  .copy--claim {
    top: 330px;
    color: var(--green-text);
    font-size: 13.5px;
    line-height: 19px;
  }
  .copy--details {
    top: 616px;
    color: var(--brown-text);
    font-size: 13.5px;
    line-height: 19px;
  }
  .copy--details p + p { margin-top: 10px; }
  .copy--details .gap { margin-top: 20px; }
</style>
</head>
<body>

  <section class="panel panel--front" aria-label="Vorderseite">
    <div class="brand">
      <span class="brand__mark"></span>
      <div class="brand__name">lindenkram.com</div>
    </div>

    <h1 class="product-title">
      <span class="product-title__type">Räucherstäbchen</span>
      <span class="product-title__variety">Weihrauch</span>
      <span class="product-title__variety">Afrika</span>
    </h1>

    <svg class="band" viewBox="0 0 268 140" aria-hidden="true">
      <path d="M0 4 Q134 -2 268 4 L268 104 Q134 40 0 104 Z" fill="var(--green)"/>
      <path d="M0 104 Q134 40 268 104 L268 116 Q134 62 0 116 Z" fill="var(--green-soft)" opacity="0.55"/>
      <path d="M0 116 Q134 62 268 116 L268 124 Q134 78 0 124 Z" fill="var(--green-soft)" opacity="0.25"/>
    </svg>
    <p class="band__claim">Made with love<br>in Germany</p>

    <div class="script-mark script-mark--front" role="img" aria-label="Handschriftlicher Schriftzug „Natur Pur“"></div>
    <div class="leaf-art" role="img" aria-label="Gezeichnete Blätter in zartem Grün"></div>

    <svg class="base" viewBox="0 0 268 150" preserveAspectRatio="none" aria-hidden="true">
      <path d="M0 0 Q60 -6 134 40 Q208 -6 268 0 L268 150 L0 150 Z" fill="var(--layer-1)"/>
      <path d="M0 30 Q70 20 134 90 Q198 20 268 30 L268 150 L0 150 Z" fill="var(--layer-2)"/>
      <path d="M0 70 Q80 60 134 130 Q188 60 268 70 L268 150 L0 150 Z" fill="var(--layer-3)"/>
      <path d="M0 110 Q90 100 134 150 Q178 100 268 110 L268 150 L0 150 Z" fill="var(--layer-4)"/>
    </svg>
  </section>

  <section class="panel panel--back" aria-label="Rückseite">
    <div class="brand">
      <span class="brand__mark"></span>
      <div class="brand__name">lindenkram.com</div>
    </div>

    <p class="copy copy--claim">
      Naturreine Räucherstäbchen<br>
      hergestellt mit den reinsten<br>
      Rohstoffen Ohne chemische oder<br>
      synthetische Zusätze, kein Parfum,<br>
      keine Abbrennhilfe
    </p>

    <svg class="band" viewBox="0 0 268 140" aria-hidden="true">
      <path d="M0 4 Q134 -2 268 4 L268 104 Q134 40 0 104 Z" fill="var(--green)"/>
      <path d="M0 104 Q134 40 268 104 L268 116 Q134 62 0 116 Z" fill="var(--green-soft)" opacity="0.55"/>
      <path d="M0 116 Q134 62 268 116 L268 124 Q134 78 0 124 Z" fill="var(--green-soft)" opacity="0.25"/>
    </svg>
    <div class="script-mark script-mark--back" role="img" aria-label="Handschriftlicher Schriftzug „Natur Pur“"></div>

    <div class="copy copy--details">
      <p>Brenndauer: ca. 45- 60min</p>
      <p>Eine Verpackung beinhaltet<br>10 Räucherstäbchen.</p>
      <p class="gap">Hergestellt von:</p>
      <p class="gap">Made by<br>Lindenkram<br>Birkenauer Weg 14<br>61287 Wiesental</p>
    </div>

    <svg class="base" viewBox="0 0 268 150" preserveAspectRatio="none" aria-hidden="true">
      <path d="M0 0 Q60 -6 134 40 Q208 -6 268 0 L268 150 L0 150 Z" fill="var(--layer-1)"/>
      <path d="M0 30 Q70 20 134 90 Q198 20 268 30 L268 150 L0 150 Z" fill="var(--layer-2)"/>
      <path d="M0 70 Q80 60 134 130 Q188 60 268 70 L268 150 L0 150 Z" fill="var(--layer-3)"/>
      <path d="M0 110 Q90 100 134 150 Q178 100 268 110 L268 150 L0 150 Z" fill="var(--layer-4)"/>
    </svg>
  </section>

</body>
</html>
```